Business Card Design for a Lending Business (Hard Money loans)

We need a business card for our Real Estate Lending business. We do hard Money loans for real estate investors. We have an existing logo we like, see attached. I'd like the business card to mostly include the logo colors, but a bright color pop of some sort would be nice to see also. Card should include Logo, Company Name, Company Address, Employee Name, Cell Phone, Main Phone, Email, Website

Industry/Entity Type

Finance / Lending

Contact Information for Business Card

Logo, Company Name, Company Address, Employee Name, Cell Phone, Main Phone, Email, Website

Requirements
Nice to have
• I'd like the business card to mostly include the logo colors, but a bright color pop of some sort would be nice to see also.

```html
<!DOCTYPE html>
<html lang="en">
<head>
<meta charset="utf-8">
<title>Crestline Lending – Business Card</title>
<link href="https://fonts.googleapis.com/css2?family=Montserrat:wght@500;600;700&family=Open+Sans:wght@400;700&display=swap" rel="stylesheet">
<style>
  :root {
    --navy: #022a8c;
    --sky: #00aee0;
    --sky-bright: #00b9ef;
    --sky-faint: #e9f7fd;
    --paper: #ffffff;
    --edge: #3b4a5e;
  }
  * { margin: 0; padding: 0; box-sizing: border-box; }
  html, body { width: 849px; height: 1200px; overflow: hidden; background: var(--paper); }
  .canvas { position: relative; width: 849px; height: 1200px; background: var(--paper); }

  .card {
    position: absolute;
    overflow: hidden;
    border-radius: 42px;
    background: var(--paper);
    border: 0.6px solid var(--edge);
  }
  .card--front { left: 125px; top: 109px; width: 475px; height: 264px; border-color: #6ccde9; }
  .card--back  { left: 252px; top: 395px; width: 475px; height: 265px; }

  .band { position: absolute; top: 0; bottom: 0; right: 0; }
  .card--front .band { left: 384px; background: linear-gradient(180deg, var(--sky-bright), var(--sky)); }
  .card--back .band  { left: 186px; background: var(--sky); }

  .wordmark {
    position: absolute;
    display: flex; flex-direction: column; align-items: center;
    font-family: "Montserrat", sans-serif;
    font-weight: 600;
    color: var(--navy);
    text-align: center;
  }
  .wordmark__dot { border-radius: 50%; background: var(--navy); }
  .wordmark__name { letter-spacing: 0.12em; line-height: 1; }
  .wordmark__sub { letter-spacing: 0.4em; line-height: 1; }

  .card--front .wordmark { left: 80px; top: 66px; width: 180px; }
  .card--front .wordmark__dot { width: 72px; height: 72px; margin-bottom: 20px; }
  .card--front .wordmark__name { font-size: 25px; }
  .card--front .wordmark__sub { font-size: 11px; margin-top: 8px; }

  .card--back .wordmark { left: 42px; top: 32px; width: 118px; }
  .card--back .wordmark__dot { width: 46px; height: 46px; margin-bottom: 12px; }
  .card--back .wordmark__name { font-size: 15.5px; }
  .card--back .wordmark__sub { font-size: 7px; margin-top: 5px; }

  .illustration-slot {
    position: absolute; left: 304px; top: 77px; width: 82px; height: 110px;
    border-radius: 40px 40px 46px 46px;
    background: linear-gradient(180deg, var(--sky-faint), #f3fbfe);
  }

  .website {
    position: absolute; left: 45px; top: 133px;
    transform: translate(-50%, -50%) rotate(-90deg);
    font-family: "Open Sans", sans-serif; font-size: 10.5px;
    color: var(--paper); white-space: nowrap;
  }

  .person {
    position: absolute; left: 55px; top: 178px;
    font-family: "Montserrat", sans-serif; line-height: 1.15;
  }
  .person__name { font-size: 14.5px; font-weight: 600; color: var(--navy); }
  .person__title { font-size: 13px; font-weight: 500; color: var(--sky); letter-spacing: 0.02em; }
  .person__phone { font-size: 13px; font-weight: 600; color: var(--sky); }

  .contact {
    position: absolute; left: 307px; top: 185px;
    font-family: "Open Sans", sans-serif; font-style: normal;
    color: var(--paper); line-height: 1.22;
  }
  .contact__street, .contact__city { font-size: 11.5px; }
  .contact__city strong { font-weight: 700; }
  .contact__email { font-size: 9.8px; }
</style>
</head>
<body>
<main class="canvas">

  <section class="card card--front" aria-label="Card front">
    <div class="wordmark">
      <span class="wordmark__dot"></span>
      <span class="wordmark__name">CRESTLINE</span>
      <span class="wordmark__sub">LENDING</span>
    </div>
    <div class="illustration-slot" role="img" aria-label="Faint line illustration of a hand holding a lightbulb with a dollar sign"></div>
    <div class="band">
      <span class="website">crestlinelending.com</span>
    </div>
  </section>

  <section class="card card--back" aria-label="Card back">
    <div class="wordmark">
      <span class="wordmark__dot"></span>
      <span class="wordmark__name">CRESTLINE</span>
      <span class="wordmark__sub">LENDING</span>
    </div>
    <div class="person">
      <p class="person__name">Dana Whitford</p>
      <p class="person__title">Lending Director</p>
      <p class="person__phone">(555) 014-2290.</p>
    </div>
    <div class="band"></div>
    <address class="contact">
      <p class="contact__street">1820 Marlow Ridge Rd.</p>
      <p class="contact__city"><strong>Fallston</strong> MD 21047</p>
      <p class="contact__email">info@CrestlineLending.com</p>
    </address>
  </section>

</main>
</body>
</html>
```